Business Card Design Project

Our organization is in need of a business card design with the use of our logo. We are looking for professional design that will embellish the image our consulting firm.

Here is a summary of what we do: Quorvent is systems consulting firm that specializes in the management, migration, and maintenance of IT infrastructure solutions.

Here is a link to my website: http://quorvent-example.com

I have attached the logo.

Target Market(s)

Organization that need IT and server support.

Industry/Entity Type

Business

```html
<!DOCTYPE html>
<html lang="en">
<head>
<meta charset="utf-8">
<title>Quorvent Business Card</title>
<link rel="stylesheet" href="https://fonts.googleapis.com/css2?family=Arimo:wght@400;700&display=swap">
<style>
  :root {
    --page-bg: #ecebe6;
    --card-white: #ffffff;
    --band-grey: #7a7a7a;
    --band-grey-dark: #6b6b6b;
    --navy: #1f2a5c;
    --orange: #ee7d2b;
    --text-white: #ffffff;
    --tagline-grey: #e6e6e6;
    --back-top: #6c6c6c;
    --back-bottom: #ababab;
  }
  * { margin: 0; padding: 0; box-sizing: border-box; }
  html, body {
    width: 1200px; height: 1146px; overflow: hidden;
    background: var(--page-bg);
    font-family: "Arimo", Arial, sans-serif;
  }
  .canvas { position: relative; width: 1200px; height: 1146px; }

  /* Front card */
  .card-front {
    position: absolute; left: 431px; top: 169px;
    width: 712px; height: 400px;
    background: var(--card-white);
  }
  .front-brand {
    position: absolute; right: 22px; top: 22px; height: 48px;
    display: flex; align-items: center;
  }
  .brand-dot { border-radius: 50%; background: var(--navy); flex: none; }
  .front-brand .brand-dot { width: 20px; height: 20px; }
  .brand-divider { background: var(--orange); flex: none; }
  .front-brand .brand-divider { width: 2px; height: 48px; margin: 0 12px 0 26px; }
  .brand-name { color: var(--navy); font-weight: 400; }
  .front-brand .brand-name { font-size: 28px; }

  .info-band {
    position: absolute; left: 0; top: 96px; width: 100%; height: 210px;
    background: linear-gradient(90deg, var(--band-grey-dark), var(--band-grey) 60%, #858585);
  }
  .person { position: absolute; right: 479px; top: 30px; text-align: right; }
  .person-name { color: var(--text-white); font-size: 40px; line-height: 1; }
  .person-title { color: var(--navy); font-size: 19px; margin-top: 2px; }
  .band-divider {
    position: absolute; left: 268px; top: 23px; width: 2px; height: 163px;
    background: var(--orange);
  }
  .contact { position: absolute; left: 294px; color: var(--text-white); font-weight: 700; font-size: 19px; line-height: 24px; }
  .contact-address { top: 66px; }
  .contact-phone { top: 106px; }
  .contact svg { position: absolute; left: 0; top: 3px; width: 18px; height: 18px; }
  .contact p { padding-left: 24px; }

  .front-web {
    position: absolute; left: 0; top: 306px; width: 100%; height: 94px;
    display: flex; align-items: center; justify-content: center;
    color: var(--navy); font-size: 21px;
  }

  /* Back card */
  .card-back {
    position: absolute; left: 191px; top: 630px;
    width: 713px; height: 400px;
    background: linear-gradient(180deg, var(--back-top), var(--back-bottom));
  }
  .back-brand {
    position: absolute; left: 85px; top: 128px; height: 138px;
    display: flex; align-items: center;
  }
  .back-brand .brand-dot { width: 60px; height: 60px; }
  .back-brand .brand-divider { width: 3px; height: 138px; margin: 0 32px 0 95px; }
  .back-brand .brand-name { font-size: 80px; line-height: 1; }
  .tagline {
    position: absolute; left: 30px; top: 306px;
    color: var(--tagline-grey); font-size: 25px; letter-spacing: 2px;
  }
  .back-web {
    position: absolute; left: 257px; top: 356px;
    color: var(--navy); font-size: 22px;
  }
</style>
</head>
<body>
<main class="canvas">
  <section class="card-front">
    <div class="front-brand">
      <span class="brand-dot"></span>
      <span class="brand-divider"></span>
      <span class="brand-name">quorvent</span>
    </div>
    <div class="info-band">
      <div class="person">
        <div class="person-name">Mr. Halden</div>
        <div class="person-title">Director</div>
      </div>
      <div class="band-divider"></div>
      <div class="contact contact-address">
        <svg viewBox="0 0 18 18" aria-hidden="true">
          <rect x="1" y="1" width="16" height="16" rx="3" fill="none" stroke="#2a3466" stroke-width="1.6"/>
          <path d="M4 9 L9 4.5 L14 9 M5.5 8 V13.5 H12.5 V8" fill="none" stroke="#2a3466" stroke-width="1.6"/>
        </svg>
        <p>4410 Larkmoor Rd, Austin, TX 78745</p>
      </div>
      <div class="contact contact-phone">
        <svg viewBox="0 0 18 18" aria-hidden="true">
          <rect x="1" y="1" width="16" height="16" rx="3" fill="none" stroke="#2a3466" stroke-width="1.6"/>
          <path d="M5 4.5 C4 6.5 6.5 11.5 11.5 13.5 L13.5 11.5 L11 10 L10 11 C8.5 10.3 7.7 9.5 7 8 L8 7 L6.5 4.5 Z" fill="#2a3466"/>
        </svg>
        <p>Toll-free in US: 888.555.0142<br>Local: 512.555.0187<br>FAX: 512.555.0188</p>
      </div>
    </div>
    <div class="front-web">www.quorvent-example.com</div>
  </section>

  <section class="card-back">
    <div class="back-brand">
      <span class="brand-dot"></span>
      <span class="brand-divider"></span>
      <span class="brand-name">quorvent</span>
    </div>
    <div class="tagline">WEB &amp; IT SYSTEM SOLUTION</div>
    <div class="back-web">www.quorvent-example.com</div>
  </section>
</main>
</body>
</html>
```